Everything fresh, everything new

When I take over the practice, I would like to breathe new life into the practice. I want a business card design that catches the eye and brings a breath of fresh air

```html
<!DOCTYPE html>
<html lang="de">
<head>
<meta charset="utf-8">
<title>Vitalwerk – Visitenkarte</title>
<link href="https://fonts.googleapis.com/css2?family=Arimo:wght@400;700&display=swap" rel="stylesheet">
<style>
  :root {
    --backdrop: #6e7b6f;
    --card: #4a4a4a;
    --lime: #8cc63f;
    --white: #ffffff;
    --muted: #d9d9d9;
    --card-w: 520px;
    --card-h: 297px;
  }
  * { margin: 0; padding: 0; box-sizing: border-box; }
  html, body {
    width: 674px;
    height: 1200px;
    overflow: hidden;
    background: var(--backdrop);
    font-family: "Arimo", Arial, sans-serif;
  }
  .sheet {
    width: 674px;
    height: 1200px;
    display: flex;
    flex-direction: column;
    align-items: center;
    justify-content: center;
    gap: 64px;
  }
  .card {
    position: relative;
    width: var(--card-w);
    height: var(--card-h);
    background: var(--card);
    box-shadow: 0 10px 18px rgba(0, 0, 0, 0.28);
    overflow: hidden;
  }

  /* Front side */
  .card-front {
    display: flex;
    flex-direction: column;
    align-items: center;
    justify-content: center;
  }
  .brand-lockup {
    display: flex;
    align-items: center;
    gap: 12px;
  }
  .brand-dot {
    width: 18px;
    height: 18px;
    border-radius: 50%;
    background: var(--lime);
  }
  .brand-name-large {
    color: var(--white);
    font-size: 44px;
    font-weight: 700;
    letter-spacing: 0.5px;
  }
  .brand-tagline {
    margin-top: 10px;
    color: var(--white);
    font-size: 12px;
    letter-spacing: 0.4px;
  }

  /* Back side */
  .person {
    position: absolute;
    left: 64px;
    top: 38px;
  }
  .person-name {
    color: var(--lime);
    font-size: 17px;
    font-weight: 700;
    letter-spacing: 0.3px;
  }
  .person-role {
    margin-top: 3px;
    color: var(--muted);
    font-size: 13px;
  }
  .brand-name-small {
    position: absolute;
    right: 62px;
    top: 116px;
    color: var(--white);
    font-size: 23px;
    font-weight: 700;
  }
  .divider {
    position: absolute;
    left: 64px;
    right: 0;
    top: 158px;
    height: 2px;
    background: var(--lime);
  }
  .contact {
    position: absolute;
    left: 64px;
    top: 176px;
    color: var(--muted);
    font-size: 13px;
    line-height: 17px;
  }
  .contact-dash {
    width: 24px;
    height: 2px;
    background: var(--lime);
    margin: 9px 0 10px;
  }
</style>
</head>
<body>
  <main class="sheet">
    <section class="card card-front" aria-label="Vorderseite">
      <div class="brand-lockup">
        <span class="brand-dot"></span>
        <span class="brand-name-large">Vitalwerk</span>
      </div>
      <p class="brand-tagline">Kraft aus Ruhe</p>
    </section>

    <section class="card card-back" aria-label="Rückseite">
      <div class="person">
        <p class="person-name">JONAS BERGER</p>
        <p class="person-role">Manager</p>
      </div>
      <p class="brand-name-small">Vitalwerk</p>
      <div class="divider"></div>
      <div class="contact">
        <p>Lindenhofweg 14</p>
        <p>42651 Feldkirchen</p>
        <div class="contact-dash"></div>
        <p>0211 485200</p>
        <p>www.vitalwerk-praxis.de</p>
      </div>
    </section>
  </main>
</body>
</html>
```